PowerPoint template for Law Firm

We Need a PowerPoint Template for a Law Firm in Switzerland. We are primarly consult in business law. We Need a template for PowerPoint to Show Information to our Clients (inheritence law, corporate law, legal structures etc.) The design should be contemporary, simple and clear. It should be in harmony with our website: www.tannquist.com Style: professional, structured and clearly arranged. Colors: Blue (R: 1, G: 61: B: 105), white. Font: Calibri Ratio: 16: 9 Esamples attached

```html
<!DOCTYPE html>
<html lang="en">
<head>
<meta charset="utf-8">
<title>Tannquist Legal – Presentation Template</title>
<link rel="stylesheet" href="https://fonts.googleapis.com/css2?family=Montserrat:wght@400;500;600;700;800&display=swap">
<style>
:root{
  --blue:#013d69;
  --blue-mid:#1f6fb8;
  --sky:#2f9bef;
  --sky-light:#7dcff0;
  --periwinkle:#5b7fd6;
  --ink:#1c1c1c;
  --grey:#9b9b9b;
  --page:#f2f2f2;
  --white:#ffffff;
}
*{margin:0;padding:0;box-sizing:border-box}
html,body{width:1200px;height:2201px;overflow:hidden}
body{background:var(--page);font-family:"Montserrat",Arial,sans-serif;color:var(--ink);position:relative}

/* hero */
.hero-slide{position:absolute;left:64px;top:51px;width:619px;height:349px;background:var(--blue)}
.hero-line-art{position:absolute;left:101px;top:152px;width:420px;height:55px;background:linear-gradient(90deg,rgba(255,255,255,0),rgba(255,255,255,.16),rgba(255,255,255,0))}

/* feature list */
.features{position:absolute;left:762px;top:30px;width:430px;height:400px;list-style:none;font-weight:800;font-size:21px;line-height:26px;color:#111;letter-spacing:.4px}
.feature{position:absolute;left:0;white-space:nowrap;list-style:none}
.feature.check{padding-left:24px}
.feature.check::before{content:"";position:absolute;left:0;top:1px;width:18px;height:18px;border:2.5px solid #111;border-radius:2px}
.feature.sub{left:56px;padding-left:18px}
.feature.sub::before{content:"";position:absolute;left:0;top:8px;width:8px;height:8px;background:#111}
.feature.cont{left:16px}
.feature.sub-cont{left:74px}

/* slides */
.slide{position:absolute;width:372px;height:209px;background:var(--white);overflow:hidden;box-shadow:0 1px 4px rgba(0,0,0,.25)}
.slide > *{position:absolute}
.col-a{left:17px}.col-b{left:416px}.col-c{left:816px}
.row-1{top:494px}.row-2{top:767px}.row-3{top:1042px}.row-4{top:1316px}.row-5{top:1590px}.row-6{top:1864px}
.brand{right:20px;bottom:9px;font-size:6.6px;font-weight:600;color:var(--blue)}
.brand.tag{background:var(--white);padding:2px 4px 1px 6px;right:14px;bottom:6px}
.toprule{right:0;top:21px;width:24px;height:1px;background:var(--blue-mid)}
.pnum{right:16px;top:13px;font-size:3.5px;color:var(--grey)}
.band{background:var(--blue)}
.ph{background:linear-gradient(135deg,#d9dde2,#8a96a6)}
.ph.warm{background:linear-gradient(135deg,#eae6e1,#6f7c8d)}
.ph.paper{background:linear-gradient(135deg,#f1f1f1,#c9ccd1)}
.title{font-weight:500;color:var(--ink);line-height:.95}
.copy{font-size:3.5px;line-height:5.4px;color:var(--grey);text-align:justify}
.on-blue .copy,.copy.light{color:rgba(255,255,255,.85)}
.dash{width:10px;height:1px;background:var(--blue-mid)}
.on-blue{background:var(--blue)}
.kicker{font-size:3px;letter-spacing:.6px;color:var(--grey);text-transform:uppercase}

/* contents */
.toc-item{left:190px;font-size:6.5px;color:var(--blue)}
.toc-item small{display:block;font-size:3.2px;color:var(--ink)}
.toc-num{position:absolute;left:-24px;top:-3px;width:14px;height:16px;border:.6px solid #ccc;font-size:5px;color:var(--ink);text-align:center;line-height:16px}

/* specialist */
.area{width:130px;font-size:5.2px;font-weight:600;color:var(--white)}
.area .copy{position:static;margin-top:3px;font-weight:400}
.area-icon{position:absolute;left:-16px;top:-1px;width:9px;height:9px;border-radius:50%;background:var(--blue-mid)}

/* associates */
.associate{width:70px;text-align:center}
.associate .ph{position:static;height:66px;margin-bottom:8px}
.associate b{font-size:4.8px;font-weight:600;display:block}
.associate i{font-style:normal;font-size:2.8px;letter-spacing:.8px;color:#bbb;display:block;margin:2px 0 5px}
.associate .copy{position:static;text-align:center}

/* org chart */
.node{height:10px;border-radius:1px;font-size:2.8px;color:var(--white);text-align:center;line-height:10px}
.n-dark{background:var(--blue)}.n-sky{background:var(--sky)}.n-light{background:var(--sky-light)}.n-mid{background:#3d8ce0}.n-peri{background:var(--periwinkle)}
.pill{height:10px;border-radius:2px;font-size:2.6px;color:var(--white);padding:1px 0 0 22px;line-height:3.8px}
.avatar{width:18px;height:18px;border-radius:3px;background:linear-gradient(135deg,#cfd4da,#6b7684)}

/* buttons */
.btn{border:.7px solid var(--blue-mid);border-radius:6px;font-size:2.8px;letter-spacing:.6px;color:var(--blue-mid);text-align:center;height:10px;line-height:9px}
.btn.solid{background:var(--white);border-color:var(--white);color:var(--blue-mid)}
.service{width:72px;text-align:center}
.service .circle{position:static;width:40px;height:40px;border-radius:50%;margin:0 auto 14px;display:flex;align-items:center;justify-content:center}
.service b{font-size:5px;font-weight:600;display:block;margin-bottom:5px}
.service .copy{position:static;text-align:center}
.service .btn{position:static;width:46px;margin:5px auto 0}
</style>
</head>
<body>

<section class="hero-slide" aria-label="Title slide">
  <div class="hero-line-art" role="img" aria-label="Fine white line drawing of a mountain ridge"></div>
</section>

<ul class="features" aria-label="Template features">
  <li class="feature check" style="top:0">Ratio 16:9</li>
  <li class="feature check" style="top:30px">Full HD</li>
  <li class="feature check" style="top:60px">Custom color pallet</li>
  <li class="feature check" style="top:91px">Custom Font -&nbsp; Easy Change</li>
  <li class="feature check" style="top:121px">Easy to edit, just drag and drop</li>
  <li class="feature cont" style="top:147px">images</li>
  <li class="feature check" style="top:177px">Can be included up to 50</li>
  <li class="feature cont" style="top:205px">slides;</li>
  <li class="feature sub" style="top:233px">Text + images (1,2,3,4) ,</li>
  <li class="feature sub-cont" style="top:260px">Text Slides</li>
  <li class="feature sub" style="top:287px">Portfolio Slides , blog slides</li>
  <li class="feature sub" style="top:313px">Text Slides, infographics</li>
  <li class="feature sub" style="top:340px">Data Slides</li>
  <li class="feature check" style="top:368px">In the sample you find 25 slides</li>
</ul>

<!-- Row 1 -->
<section class="slide col-a row-1">
  <svg style="left:0;top:0" width="372" height="209"><polygon points="0,0 48,0 152,209 0,209" fill="#013d69"/></svg>
  <div class="ph paper" style="left:26px;top:46px;width:134px;height:132px" role="img" aria-label="Framed abstract line artwork on a wall"></div>
  <div class="toprule"></div>
  <div class="title" style="right:22px;top:52px;font-size:17px">About</div>
  <div style="right:22px;top:74px;font-size:10.5px;font-weight:500;color:var(--blue)">Tannquist Legal</div>
  <div class="dash" style="right:22px;top:89px"></div>
  <p class="copy" style="left:186px;top:99px;width:164px">We guide owners and boards through contract, company and trade law, with fast replies, firm discretion and steady counsel for every step of growth. We guide owners and boards through contract, company and trade law, with fast replies, firm discretion and steady counsel for every step of growth.</p>
</section>

<section class="slide col-b row-1">
  <div class="band" style="left:0;top:0;width:132px;height:209px"></div>
  <div style="left:22px;top:92px;font-size:18px;font-weight:500;color:var(--white)">Contents</div>
  <div class="toprule"></div><div class="pnum">2</div>
  <div class="toc-item" style="top:34px"><span class="toc-num">1</span>Introduction<small>Before starting</small></div>
  <div class="toc-item" style="top:66px"><span class="toc-num">2</span>About us<small>What we did, what we do</small></div>
  <div class="toc-item" style="top:98px"><span class="toc-num">3</span>Our portfolio<small>Our amazing products</small></div>
  <div class="toc-item" style="top:130px"><span class="toc-num">4</span>New proposal<small>Our awesome ideas</small></div>
  <div class="toc-item" style="top:162px"><span class="toc-num">5</span>Analysis<small>Marketing data and our estimation</small></div>
  <div class="brand">Tannquist Legal</div>
</section>

<section class="slide col-c row-1">
  <div class="title" style="left:30px;top:36px;font-size:16px">What<br>makes us<br>different?</div>
  <p class="copy" style="left:30px;top:92px;width:103px">We guide owners and boards through contract, company and trade law, with fast replies, firm discretion and steady counsel for every step of growth. We guide owners and boards through contract, company and trade law, with fast replies, firm discretion and steady counsel for every step of growth.</p>
  <div style="left:16px;top:188px;width:1px;height:21px;background:var(--blue-mid)"></div>
  <div class="band" style="left:163px;top:0;width:129px;height:209px"></div>
  <div class="ph warm" style="left:207px;top:59px;width:146px;height:100px" role="img" aria-label="Lawyers in a meeting in a bright office"></div>
  <div class="toprule"></div><div class="pnum">4</div>
  <div class="brand tag">Tannquist Legal</div>
</section>

<!-- Row 2 -->
<section class="slide col-a row-2">
  <div class="title" style="left:24px;top:42px;font-size:15.5px">Optimum<br>guidance in<br>matters of<br>commercial<br>law – and<br>beyond</div>
  <div class="dash" style="left:114px;top:157px"></div>
  <p class="copy" style="left:163px;top:44px;width:129px">We guide owners and boards through contract, company and trade law, with fast replies, firm discretion and steady counsel for every step of growth. We guide owners and boards through contract, company and trade law, with fast replies, firm discretion and steady counsel for every step of growth. We guide owners and boards through contract, company and trade law, with fast replies, firm discretion and steady counsel for every step of growth. Where in your business do you have legal issues we can tackle?</p>
  <div class="band" style="left:163px;top:156px;width:115px;height:53px"></div>
  <div class="toprule"></div>
  <div class="brand tag">Tannquist Legal</div>
</section>

<section class="slide col-b row-2 on-blue">
  <div style="left:16px;top:0;width:1px;height:36px;background:var(--blue-mid)"></div>
  <div style="left:33px;top:28px;font-size:17px;font-weight:500;color:var(--white);line-height:.95">Specialist area<br>commercial law:</div>
  <div class="pnum" style="color:#fff">7</div>
  <div class="area" style="left:51px;top:72px"><span class="area-icon"></span>Corporate law<p class="copy">Clear advice on deals, rules and risk for firms of every size, from first draft to final signing.</p></div>
  <div class="area" style="left:221px;top:72px"><span class="area-icon"></span>Labour law<p class="copy">Clear advice on deals, rules and risk for firms of every size, from first draft to final signing.</p></div>
  <div class="area" style="left:51px;top:114px"><span class="area-icon"></span>Mergers and acquisitions<p class="copy">Clear advice on deals, rules and risk for firms of every size, from first draft to final signing.</p></div>
  <div class="area" style="left:221px;top:114px"><span class="area-icon"></span>Financial and Market Capital Law<p class="copy">Clear advice on deals, rules and risk for firms of every size, from first draft to final signing.</p></div>
  <div class="area" style="left:51px;top:155px"><span class="area-icon"></span>Commercial and contrac law<p class="copy">Clear advice on deals, rules and risk for firms of every size, from first draft to final signing.</p></div>
  <div class="area" style="left:221px;top:155px"><span class="area-icon"></span>Digital economy, IT law, Data protection Law<p class="copy">Clear advice on deals, rules and risk for firms of every size, from first draft to final signing.</p></div>
</section>

<section class="slide col-c row-2">
  <p class="copy" style="left:33px;top:54px;width:96px">We guide owners and boards through contract, company and trade law, with fast replies, firm discretion and steady counsel for every step of growth. We guide owners and boards through contract, company and trade law, with fast replies, firm discretion and steady counsel for every step of growth. We guide owners and boards through contract, company and trade law, with fast replies, firm discretion and steady counsel for every step of growth.</p>
  <div style="left:16px;top:188px;width:1px;height:21px;background:var(--blue-mid)"></div>
  <div class="band" style="left:163px;top:0;width:129px;height:209px"></div>
  <div class="ph paper" style="left:207px;top:60px;width:146px;height:101px" role="img" aria-label="Hands signing a contract with a pen"></div>
  <div class="toprule"></div><div class="pnum">8</div>
  <div class="brand tag">Tannquist Legal</div>
</section>

<!-- Row 3 -->
<section class="slide col-a row-3">
  <div class="title" style="left:24px;top:42px;font-size:13px">Unique<br>and<br>sophisticated</div>
  <p class="copy" style="left:24px;top:90px;width:128px">We guide owners and boards through contract, company and trade law, with fast replies, firm discretion and steady counsel for every step of growth. We guide owners and boards through contract, company and trade law, with fast replies, firm discretion and steady counsel for every step of growth.</p>
  <div class="dash" style="left:114px;top:157px"></div>
  <div class="band" style="left:163px;top:0;width:122px;height:209px"></div>
  <div class="copy light" style="left:170px;top:37px;width:108px">We guide owners and boards through contract, company and trade law, with fast replies, firm discretion and steady counsel for every step of growth. We guide owners and boards through contract, company and trade law, with fast replies, firm discretion and steady counsel for every step of growth. We guide owners and boards through contract, company and trade law, with fast replies, firm discretion and steady counsel for every step of growth.<br>• Clear advice on deals, rules and risk for firms of every size, from first draft to final signing.<br>• Clear advice on deals, rules and risk for firms of every size, from first draft to final signing.<br>• Clear advice on deals, rules and risk for firms of every size, from first draft to final signing.</div>
  <div class="toprule"></div>
  <div class="brand tag">Tannquist Legal</div>
</section>

<section class="slide col-b row-3">
  <svg style="left:0;top:0" width="372" height="209"><polygon points="0,0 48,0 152,209 0,209" fill="#013d69"/></svg>
  <div class="ph warm" style="left:26px;top:46px;width:134px;height:132px" role="img" aria-label="Portrait of a lawyer in a dark suit"></div>
  <div class="toprule"></div>
  <div class="title" style="right:22px;top:45px;font-size:13px">Matthias Ammann</div>
  <div style="right:58px;top:62px;font-size:5.5px;color:var(--grey)">Lawyer and Notary</div>
  <div class="dash" style="left:198px;top:72px"></div>
  <div class="copy" style="left:187px;top:77px;width:164px;line-height:5px">We guide owners and boards through contract, company and trade law, with fast replies, firm discretion and steady counsel for every step of growth. We guide owners and boards through contract, company and trade law, with fast replies, firm discretion and steady counsel for every step of growth.<br><span style="color:var(--blue)">Experience</span><br>Partner at a Zurich firm (2012)<br><span style="color:var(--blue)">Education</span><br>Master of Law, University of Bern (2007)</div>
  <div class="brand">Tannquist Legal</div>
</section>

<section class="slide col-c row-3">
  <div class="title" style="left:33px;top:42px;font-size:18px">Title text demo</div>
  <div class="dash" style="left:33px;top:62px"></div>
  <div class="toprule"></div><div class="pnum">10</div>
  <div class="ph paper" style="left:33px;top:82px;width:94px;height:72px" role="img" aria-label="Document and fountain pen on a desk"></div>
  <div class="ph warm" style="left:139px;top:82px;width:94px;height:72px" role="img" aria-label="Lawyers in a meeting"></div>
  <div class="ph paper" style="left:245px;top:82px;width:94px;height:72px" role="img" aria-label="Hands signing a contract"></div>
  <p class="copy" style="left:33px;top:160px;width:94px;text-align:center">Short note about this image and its use here.</p>
  <p class="copy" style="left:139px;top:160px;width:94px;text-align:center">Short note about this image and its use here.</p>
  <p class="copy" style="left:245px;top:160px;width:94px;text-align:center">Short note about this image and its use here.</p>
  <div class="brand">Tannquist Legal</div>
</section>

<!-- Row 4 -->
<section class="slide col-a row-4">
  <div class="band" style="left:36px;top:0;width:108px;height:209px"></div>
  <div class="toprule"></div><div class="pnum">11</div>
  <div class="kicker" style="left:185px;top:34px">Demo slide</div>
  <div class="title" style="left:185px;top:40px;font-size:18px">Title text<br>demo</div>
  <div class="dash" style="left:185px;top:76px"></div>
  <p class="copy" style="left:185px;top:84px;width:165px">We guide owners and boards through contract, company and trade law, with fast replies, firm discretion and steady counsel for every step of growth. We guide owners and boards through contract, company and trade law, with fast replies, firm discretion and steady counsel for every step of growth. We guide owners and boards through contract, company and trade law, with fast replies, firm discretion and steady counsel for every step of growth. We guide owners and boards through contract, company and trade law, with fast replies, firm discretion and steady counsel for every step of growth.</p>
  <div class="brand">Tannquist Legal</div>
</section>

<section class="slide col-b row-4">
  <div style="left:21px;top:10px;font-size:9.5px;font-weight:600;color:var(--blue)">Our associates lawyers</div>
  <div class="toprule"></div><div class="pnum">16</div>
  <div class="associate" style="left:32px;top:44px"><div class="ph warm" role="img" aria-label="Portrait of an associate lawyer"></div><b>Helen Stark</b><i>Manager</i><p class="copy">Clear advice on deals, rules and risk for firms of every size, from first draft to final signing.</p></div>
  <div class="associate" style="left:111px;top:44px"><div class="ph warm" role="img" aria-label="Portrait of an associate lawyer"></div><b>Max Falk</b><i>Manager</i><p class="copy">Clear advice on deals, rules and risk for firms of every size, from first draft to final signing.</p></div>
  <div class="associate" style="left:190px;top:44px"><div class="ph warm" role="img" aria-label="Portrait of an associate lawyer"></div><b>Andy Freeman</b><i>Manager</i><p class="copy">Clear advice on deals, rules and risk for firms of every size, from first draft to final signing.</p></div>
  <div class="associate" style="left:269px;top:44px"><div class="ph warm" role="img" aria-label="Portrait of an associate lawyer"></div><b>Lory Lee</b><i>Manager</i><p class="copy">Clear advice on deals, rules and risk for firms of every size, from first draft to final signing.</p></div>
  <div class="brand">Tannquist Legal</div>
</section>

<section class="slide col-c row-4 on-blue">
  <div class="pnum" style="color:#fff">13</div>
  <div class="kicker" style="left:0;width:372px;text-align:center;top:48px;color:rgba(255,255,255,.5)">Demo slide</div>
  <div style="left:0;width:372px;text-align:center;top:54px;font-size:18px;font-weight:500;color:var(--white)">Title text demo</div>
  <p class="copy" style="left:98px;top:92px;width:176px;text-align:center">We guide owners and boards through contract, company and trade law, with fast replies, firm discretion and steady counsel for every step of growth. We guide owners and boards through contract, company and trade law, with fast replies, firm discretion and steady counsel for every step of growth.</p>
  <div class="btn solid" style="left:162px;top:160px;width:48px">NEW PROJECT</div>
</section>

<!-- Row 5 -->
<section class="slide col-a row-5">
  <div style="left:21px;top:11px;font-size:9.5px;font-weight:600;color:var(--blue)">Organization Structure</div>
  <div class="toprule"></div>
  <svg style="left:0;top:0" width="372" height="209" fill="none" stroke="#333" stroke-width=".5">
    <path d="M178 53v14M178 77v12M74 89h247M74 89v4M151 89v4M227 89v4M280 89v4"/>
    <path d="M66 103v60h5M66 143h5M66 123h5M141 103v20M188 103v20M218 103v78h5M218 123h5M218 143h5M218 163h5M270 103v40h5M270 123h5"/>
  </svg>
  <div class="node n-dark" style="left:154px;top:43px;width:48px">General Manager</div>
  <div class="node n-dark" style="left:158px;top:67px;width:40px">Assistant</div>
  <div class="node n-sky" style="left:52px;top:93px;width:45px">Sales</div>
  <div class="node n-light" style="left:128px;top:93px;width:45px">Production</div>
  <div class="node n-sky" style="left:204px;top:93px;width:45px">Finance</div>
  <div class="node n-peri" style="left:257px;top:93px;width:48px">Supply Chain</div>
  <div class="node n-sky" style="left:54px;top:106px;width:42px"></div>
  <div class="node n-sky" style="left:66px;top:126px;width:42px"></div>
  <div class="node n-sky" style="left:66px;top:146px;width:42px"></div>
  <div class="node n-light" style="left:104px;top:106px;width:42px"></div>
  <div class="node n-light" style="left:116px;top:126px;width:42px"></div>
  <div class="node n-light" style="left:155px;top:106px;width:42px"></div>
  <div class="node n-light" style="left:167px;top:126px;width:42px"></div>
  <div class="node n-mid" style="left:223px;top:106px;width:42px"></div>
  <div class="node n-mid" style="left:223px;top:126px;width:42px"></div>
  <div class="node n-mid" style="left:223px;top:146px;width:42px"></div>
  <div class="node n-mid" style="left:223px;top:166px;width:42px"></div>
  <div class="node n-peri" style="left:275px;top:106px;width:48px"></div>
  <div class="node n-peri" style="left:275px;top:126px;width:48px"></div>
  <div class="brand">Tannquist Legal</div>
</section>

<section class="slide col-b row-5">
  <div style="left:21px;top:11px;font-size:9.5px;font-weight:600;color:var(--blue)">Organization Structure</div>
  <div class="toprule"></div>
  <svg style="left:0;top:0" width="372" height="209" fill="none" stroke="#333" stroke-width=".5">
    <path d="M115 109h12v-18h8M127 109v18h8M190 91h10v-10h8M200 91v10h8M260 101h8M190 127h10v-10h8M200 127v24h8M260 127h8"/>
  </svg>
  <div class="pill n-dark" style="left:65px;top:103px;width:50px">Jhon Sam<br>CEO</div><div class="avatar" style="left:62px;top:100px" role="img" aria-label="Staff portrait"></div>
  <div class="pill n-dark" style="left:137px;top:85px;width:52px">John Smith<br>Manager</div><div class="avatar" style="left:134px;top:82px" role="img" aria-label="Staff portrait"></div>
  <div class="pill n-dark" style="left:137px;top:121px;width:52px">Alex Day<br>Manager</div><div class="avatar" style="left:134px;top:118px" role="img" aria-label="Staff portrait"></div>
  <div class="pill n-sky" style="left:211px;top:68px;width:48px">Patrick<br>General Manager</div><div class="avatar" style="left:208px;top:65px" role="img" aria-label="Staff portrait"></div>
  <div class="pill n-sky" style="left:211px;top:94px;width:48px">James<br>General Manager</div><div class="avatar" style="left:208px;top:91px" role="img" aria-label="Staff portrait"></div>
  <div class="pill n-sky" style="left:211px;top:119px;width:48px">Noel<br>General Manager</div><div class="avatar" style="left:208px;top:116px" role="img" aria-label="Staff portrait"></div>
  <div class="pill n-mid" style="left:211px;top:143px;width:48px">Jessica<br>General Manager</div><div class="avatar" style="left:208px;top:140px" role="img" aria-label="Staff portrait"></div>
  <div class="pill n-sky" style="left:275px;top:94px;width:44px">Jackie<br>Member</div><div class="avatar" style="left:272px;top:91px" role="img" aria-label="Staff portrait"></div>
  <div class="pill n-sky" style="left:275px;top:119px;width:44px">Ericka<br>Member</div><div class="avatar" style="left:272px;top:116px" role="img" aria-label="Staff portrait"></div>
  <div class="brand">Tannquist Legal</div>
</section>

<section class="slide col-c row-5">
  <svg style="left:0;top:0" width="372" height="209"><polygon points="0,0 48,0 152,209 0,209" fill="#013d69"/></svg>
  <div class="ph paper" style="left:46px;top:54px;width:110px;height:103px" role="img" aria-label="Abstract line artwork on paper"></div>
  <div class="toprule"></div><div class="pnum">12</div>
  <div class="title" style="left:194px;top:42px;font-size:17px">Title text<br>demo</div>
  <div class="dash" style="left:194px;top:82px"></div>
  <p class="copy" style="left:194px;top:90px;width:132px">We guide owners and boards through contract, company and trade law, with fast replies, firm discretion and steady counsel for every step of growth. We guide owners and boards through contract, company and trade law, with fast replies, firm discretion and steady counsel for every step of growth. We guide owners and boards through contract, company and trade law, with fast replies, firm discretion and steady counsel for every step of growth.</p>
  <div class="brand">Tannquist Legal</div>
</section>

<!-- Row 6 -->
<section class="slide col-a row-6">
  <div class="title" style="left:33px;top:40px;font-size:18px">Text two column</div>
  <div class="toprule"></div>
  <p class="copy" style="left:33px;top:70px;width:148px">We guide owners and boards through contract, company and trade law, with fast replies, firm discretion and steady counsel for every step of growth. We guide owners and boards through contract, company and trade law, with fast replies, firm discretion and steady counsel for every step of growth. We guide owners and boards through contract, company and trade law, with fast replies, firm discretion and steady counsel for every step of growth.</p>
  <p class="copy" style="left:188px;top:70px;width:148px">We guide owners and boards through contract, company and trade law, with fast replies, firm discretion and steady counsel for every step of growth. We guide owners and boards through contract, company and trade law, with fast replies, firm discretion and steady counsel for every step of growth. We guide owners and boards through contract, company and trade law, with fast replies, firm discretion and steady counsel for every step of growth.</p>
  <div class="brand">Tannquist Legal</div>
</section>

<section class="slide col-b row-6">
  <div class="title" style="left:33px;top:40px;font-size:18px">Single text slide</div>
  <div class="toprule"></div>
  <p class="copy" style="left:33px;top:70px;width:310px">We guide owners and boards through contract, company and trade law, with fast replies, firm discretion and steady counsel for every step of growth. We guide owners and boards through contract, company and trade law, with fast replies, firm discretion and steady counsel for every step of growth. We guide owners and boards through contract, company and trade law, with fast replies, firm discretion and steady counsel for every step of growth.</p>
  <p class="copy" style="left:33px;top:104px;width:310px">We guide owners and boards through contract, company and trade law, with fast replies, firm discretion and steady counsel for every step of growth. We guide owners and boards through contract, company and trade law, with fast replies, firm discretion and steady counsel for every step of growth. We guide owners and boards through contract, company and trade law, with fast replies, firm discretion and steady counsel for every step of growth.</p>
  <p class="copy" style="left:33px;top:138px;width:310px">We guide owners and boards through contract, company and trade law, with fast replies, firm discretion and steady counsel for every step of growth. We guide owners and boards through contract, company and trade law, with fast replies, firm discretion and steady counsel for every step of growth.</p>
  <div class="brand">Tannquist Legal</div>
</section>

<section class="slide col-c row-6">
  <div class="toprule"></div><div class="pnum">19</div>
  <div class="service" style="left:29px;top:42px">
    <div class="circle" style="background:var(--blue)"><svg width="14" height="14" viewBox="0 0 14 14"><path d="M4 6V4.5a3 3 0 016 0V6" fill="none" stroke="#fff" stroke-width="1.5"/><rect x="3" y="6" width="8" height="6.5" rx="1" fill="#fff"/></svg></div>
    <b>Project Name</b><p class="copy">Clear advice on deals, rules and risk for firms of every size, from first draft to final signing.</p><div class="btn">NEW PROJECT</div></div>
  <div class="service" style="left:109px;top:42px">
    <div class="circle" style="background:#1e8ff0"><svg width="14" height="14" viewBox="0 0 14 14"><path d="M1 2h2l1.5 7h7L13 4H4" fill="none" stroke="#fff" stroke-width="1.4"/><circle cx="5.5" cy="11.8" r="1" fill="#fff"/><circle cx="10.5" cy="11.8" r="1" fill="#fff"/></svg></div>
    <b>Project Name</b><p class="copy">Clear advice on deals, rules and risk for firms of every size, from first draft to final signing.</p><div class="btn">NEW PROJECT</div></div>
  <div class="service" style="left:189px;top:42px">
    <div class="circle" style="background:#56aef0"><svg width="14" height="14" viewBox="0 0 14 14"><rect x="1" y="6" width="3" height="7" fill="#fff"/><path d="M5 6l3-5c1.2 0 1.6.8 1.3 2L9 5h3.2c.8 0 1.3.7 1.1 1.4l-1.3 5.4c-.2.6-.7 1.2-1.4 1.2H5z" fill="#fff"/></svg></div>
    <b>Project Name</b><p class="copy">Clear advice on deals, rules and risk for firms of every size, from first draft to final signing.</p><div class="btn">NEW PROJECT</div></div>
  <div class="service" style="left:269px;top:42px">
    <div class="circle" style="background:#bfe3fb"><svg width="14" height="14" viewBox="0 0 14 14"><path d="M3 1.5l2.2 0 1 3-1.5 1.2a8 8 0 003.6 3.6l1.2-1.5 3 1v2.2c0 .7-.6 1.2-1.3 1.2A11 11 0 011.8 2.8c0-.7.5-1.3 1.2-1.3z" fill="#fff"/></svg></div>
    <b>Project Name</b><p class="copy">Clear advice on deals, rules and risk for firms of every size, from first draft to final signing.</p><div class="btn">NEW PROJECT</div></div>
  <div class="brand">Tannquist Legal</div>
</section>

</body>
</html>
```